Front signage

Our work consists of Industrial Electrical Automation.
We are an established company with a logo we are happy with.
Though we still need:
- a sign for our front door - 420mm x 1200mm
- a sign at the front of the building - 250mm x 1600mm

Please see attached our logo, and following our colour theme would be nice, but not essential.
Please see our website for more information on what we do
www.voltarispan.com.au

```html
<!DOCTYPE html>
<html lang="en">
<head>
<meta charset="utf-8">
<title>Voltarispan Power Group – Front Signage</title>
<link rel="stylesheet" href="https://fonts.googleapis.com/css2?family=Archivo+Black&family=Archivo:wght@500;600;800&display=swap">
<style>
  :root {
    --page: #e4e4e4;
    --sign-bg: #ebebeb;
    --grey: #4d4d4f;
    --blue: #0a4aa0;
    --orange: #f0531f;
    --white: #ffffff;
    --social-dot: #5b7fc0;
    --photo-dark: #2b2e33;
    --photo-mid: #7d8188;
    --photo-light: #d9dadc;
  }
  * { margin: 0; padding: 0; box-sizing: border-box; }
  html, body { width: 1200px; height: 1200px; overflow: hidden; background: var(--page); }
  .sign {
    position: absolute; left: 30px; top: 400px;
    width: 1140px; height: 399px;
    background: var(--sign-bg);
    overflow: hidden;
    font-family: "Archivo", Arial, sans-serif;
  }
  .sign-shapes { position: absolute; inset: 0; }
  .brand-mark {
    position: absolute; left: 853px; top: 62px; transform: translateX(-50%);
    display: flex; align-items: center; gap: 14px; white-space: nowrap;
  }
  .brand-mark__name {
    font-family: "Archivo Black", Arial, sans-serif;
    font-size: 54px; line-height: 1; color: var(--grey); letter-spacing: 1px;
  }
  .brand-mark__dot { width: 26px; height: 26px; border-radius: 50%; background: var(--blue); }
  .company-name {
    position: absolute; left: 599px; width: 510px; top: 183px;
    text-align: center; white-space: nowrap;
    font-family: "Archivo Black", Arial, sans-serif;
    font-size: 27px; letter-spacing: 1.5px; color: var(--grey); font-weight: 400;
  }
  .company-name__accent { color: var(--blue); }
  .tagline {
    position: absolute; left: 599px; width: 510px; top: 220px;
    display: flex; align-items: center; gap: 10px;
    color: var(--orange); font-weight: 600; font-size: 11.5px; letter-spacing: 1.6px;
    white-space: nowrap;
  }
  .tagline::before, .tagline::after { content: ""; flex: 1; height: 1.5px; background: var(--orange); }
  .mission-rules {
    position: absolute; left: 645px; width: 420px; top: 258px; height: 62px;
    border-top: 1.5px solid var(--blue); border-bottom: 1.5px solid var(--blue);
  }
  .mission {
    position: absolute; left: 585px; width: 540px; top: 264px;
    text-align: center; font-family: "Archivo Black", Arial, sans-serif;
    font-size: 13.6px; line-height: 16.6px; letter-spacing: 0.2px;
    color: var(--blue); white-space: nowrap;
  }
  .mission__lead { color: var(--grey); }
  .contact-bar {
    position: absolute; left: 524px; top: 354px; height: 45px;
    display: flex; align-items: center; gap: 18px;
    color: var(--white); font-weight: 600; font-size: 22.5px;
  }
  .contact-bar__divider { width: 1.5px; height: 30px; background: var(--white); }
  .contact-bar__social { display: flex; align-items: center; gap: 12px; }
  .contact-bar__dot { width: 26px; height: 26px; border-radius: 50%; background: var(--social-dot); }
</style>
</head>
<body>
  <div class="sign">
    <svg class="sign-shapes" width="1140" height="399" viewBox="0 0 1140 399">
      <defs>
        <linearGradient id="plantTones" x1="0" y1="0" x2="1" y2="1">
          <stop offset="0" stop-color="#2b2e33"/>
          <stop offset="0.45" stop-color="#d9dadc"/>
          <stop offset="0.75" stop-color="#7d8188"/>
          <stop offset="1" stop-color="#2b2e33"/>
        </linearGradient>
      </defs>
      <polygon points="488,0 510,0 588,324 432,399 391,399 566,312" fill="#f0531f"/>
      <polygon points="0,0 488,0 566,312 391,399 0,399" fill="url(#plantTones)" role="img" aria-label="Black and white photograph of an industrial plant with pipework, steel towers and walkways"/>
      <polygon points="514,354 1092,354 1127,399 432,399" fill="#0a4aa0"/>
    </svg>

    <div class="brand-mark">
      <span class="brand-mark__name">VOLTARISPAN</span>
      <span class="brand-mark__dot"></span>
    </div>

    <h1 class="company-name">VOLTARISPAN <span class="company-name__accent">POWER</span> GROUP</h1>

    <p class="tagline">INDUSTRIAL ELECTRICAL AND MECHANICAL SERVICES</p>

    <div class="mission-rules"></div>
    <p class="mission">
      <span class="mission__lead">DEVELOPING INNOVATIVE SOLUTIONS TO YOUR</span><br>
      COMPANY’S NEEDS, IN INDUSTRIAL AUTOMATION,<br>
      ELECTRICAL AND MECHANICAL PROJECTS AND BREAKDOWNS.
    </p>

    <div class="contact-bar">
      <span class="contact-bar__web">www.voltarispan.com.au</span>
      <span class="contact-bar__divider"></span>
      <span class="contact-bar__social">Follow Us <span class="contact-bar__dot"></span></span>
    </div>
  </div>
</body>
</html>
```